Brindel Clear Springs needs a new business card design (we produce and sell pure bottled water)

We need a clean modern design for our new business cards, We have an existing logo which ultimately cannot be changed, however it could be slighty improved and the colours adjusted. We have this existing logo on all of our bottles, vehicles etc.

Our company slogan is "Pure down to the last drop".
Along with our relevant company information
(Address, phone, website email etc) we will only be using names and not putting position titles for flexibilty.

We are looking for a clean, minimalist modern design.

You can view our website (if need of an update also!) to see our business.

Industry/Entity Type

Business

Contact Information for Business Card

Staff Name : XXXXXX XXXXXX
Address : 8/41 Tallowood St
Marwick Flats QLD 4172
Staff Mobile Number : 04XX XXX XXX
Office Phone Number : 07 3918 4520
Staff Email Address : XXXX@brindelclearsprings.com.au
Website : www.brindelclearsprings.com.au

Font styles to use
Sans Serif

Colors
cee9f5
33a6d7
0492cd
0455a3
3276b5
85abd2
cedeed

Requirements
Must have
• The ability to edit and change the staff members details as we will need to edit for each respective staff member (7 in total)

```html
<!DOCTYPE html>
<html lang="en">
<head>
<meta charset="utf-8">
<title>Brindel Clear Springs – Business Card</title>
<link href="https://fonts.googleapis.com/css2?family=Arimo:wght@400;700&display=swap" rel="stylesheet">
<style>
  :root {
    --page-bg: #e0e2e2;
    --card-white: #ffffff;
    --card-dark: #1c1d1d;
    --navy: #2b3590;
    --mist: #cde0ef;
    --drop: #bcd6ea;
    --ink: #1d1d1d;
    --ink-soft: #333333;
    --light: #f2f2f2;
  }
  * { box-sizing: border-box; margin: 0; padding: 0; }
  html, body { width: 960px; height: 1200px; overflow: hidden; }
  body {
    background: var(--page-bg);
    font-family: "Arimo", Arial, sans-serif;
    position: relative;
  }
  .card {
    position: absolute;
    left: 80px;
    width: 800px;
    height: 440px;
    border-radius: 28px;
    overflow: hidden;
    box-shadow: 0 6px 18px rgba(0,0,0,0.18);
  }
  .card-front { top: 110px; background: var(--card-white); }
  .card-back  { top: 650px; background: var(--card-dark); }

  .front-wave { position: absolute; left: 0; bottom: 0; width: 800px; height: 440px; }

  .brand-name {
    position: absolute;
    right: 44px;
    top: 48px;
    display: flex;
    align-items: center;
    gap: 12px;
    color: var(--navy);
    font-weight: 700;
    font-size: 28px;
  }
  .brand-dot { width: 18px; height: 18px; border-radius: 50%; background: var(--navy); }

  .staff { position: absolute; left: 44px; top: 150px; }
  .staff-name { font-size: 34px; font-weight: 700; color: var(--ink); letter-spacing: 0.5px; }
  .staff-rule { position: absolute; left: -20px; top: 48px; width: 300px; height: 40px; }
  .staff-role { font-size: 28px; color: var(--ink-soft); margin-top: 14px; }

  .contact { position: absolute; display: flex; flex-direction: column; gap: 12px; }
  .contact-left { left: 40px; top: 352px; }
  .contact-right { left: 300px; top: 316px; }
  .contact-item { display: flex; align-items: center; gap: 12px; font-size: 18px; color: var(--ink); }
  .contact-icon { width: 22px; height: 22px; flex: none; }

  .back-inner {
    position: absolute; inset: 0;
    display: flex; flex-direction: column; align-items: center; justify-content: center;
    color: var(--light);
  }
  .slogan { font-size: 19px; letter-spacing: 0.4px; margin-bottom: 10px; }
  .back-frame { position: relative; width: 320px; height: 160px; display: flex; align-items: center; justify-content: center; }
  .back-frame svg { position: absolute; inset: 0; }
  .back-brand { font-size: 26px; font-weight: 700; color: #6f73c4; }
  .website { font-size: 19px; letter-spacing: 0.4px; margin-top: 14px; }
</style>
</head>
<body>

<section class="card card-front" aria-label="Business card front">
  <svg class="front-wave" viewBox="0 0 800 440" aria-hidden="true">
    <path fill="var(--mist)" d="M0 340 C40 320 70 325 100 318 C140 300 170 318 210 305 C260 296 300 300 340 290 C400 282 440 288 480 275 C520 262 560 258 600 245 C640 226 680 238 720 222 C750 215 780 220 800 218 L800 440 L0 440 Z"/>
    <rect fill="var(--navy)" x="0" y="414" width="800" height="26"/>
  </svg>

  <div class="brand-name"><span class="brand-dot"></span>Brindel Clear Springs</div>

  <div class="staff">
    <div class="staff-name">JOHN DOE</div>
    <svg class="staff-rule" viewBox="0 0 300 40" aria-hidden="true">
      <line x1="0" y1="12" x2="262" y2="2" stroke="var(--drop)" stroke-width="2"/>
      <path fill="var(--drop)" d="M270 6 C274 14 284 22 284 30 A11 11 0 0 1 262 30 C262 22 268 14 270 6 Z"/>
    </svg>
    <div class="staff-role">Manager</div>
  </div>

  <div class="contact contact-left">
    <div class="contact-item">
      <svg class="contact-icon" viewBox="0 0 22 22" aria-hidden="true"><circle cx="11" cy="11" r="11" fill="var(--navy)"/><rect x="7.5" y="5" width="7" height="12" rx="1.5" fill="none" stroke="#fff" stroke-width="1.6"/></svg>
      04XX XXX XXX
    </div>
    <div class="contact-item">
      <svg class="contact-icon" viewBox="0 0 22 22" aria-hidden="true"><circle cx="11" cy="11" r="11" fill="var(--navy)"/><path fill="#fff" d="M5 9 C5 6 17 6 17 9 L15 10 L14 8.5 L8 8.5 L7 10 Z M7 11 L15 11 L16 15 L6 15 Z"/></svg>
      07 3918 4520
    </div>
  </div>

  <div class="contact contact-right">
    <div class="contact-item">
      <svg class="contact-icon" viewBox="0 0 22 22" aria-hidden="true"><circle cx="11" cy="11" r="11" fill="var(--navy)"/><rect x="5.5" y="7" width="11" height="8" rx="1" fill="#fff"/><path d="M5.5 7.5 L11 11.5 L16.5 7.5" fill="none" stroke="var(--navy)" stroke-width="1.2"/></svg>
      XXXX@brindelclearsprings.com.au
    </div>
    <div class="contact-item">
      <svg class="contact-icon" viewBox="0 0 22 22" aria-hidden="true"><circle cx="11" cy="11" r="11" fill="var(--navy)"/><path fill="#fff" d="M11 4.5 A4.5 4.5 0 0 1 15.5 9 C15.5 12 11 17.5 11 17.5 C11 17.5 6.5 12 6.5 9 A4.5 4.5 0 0 1 11 4.5 Z"/><circle cx="11" cy="9" r="1.8" fill="var(--navy)"/></svg>
      8/41 Tallowood St, Marwick Flats QLD 4172
    </div>
  </div>
</section>

<section class="card card-back" aria-label="Business card back">
  <div class="back-inner">
    <p class="slogan">Pure down to the last drop</p>
    <div class="back-frame">
      <svg viewBox="0 0 320 160" aria-hidden="true">
        <polyline points="1,160 1,1 319,1 319,160" fill="none" stroke="var(--light)" stroke-width="2"/>
      </svg>
      <span class="back-brand">Brindel Clear Springs</span>
    </div>
    <p class="website">www.brindelclearsprings.com.au</p>
  </div>
</section>

</body>
</html>
```